Project Brightvale Remedies

We need a business/ logo card design for our company based out of Canada. We will be retailing cannibus products to our customers.
For colors I've found this online : https://www.pallortune.edu/shade-picker-output/?tones=70ff02,ff0270,ff4a02,02e1ff . We especially like the green and blue .
We would like our business card design to communicate modern medicine .

Target Market(s)

males 20-40 years

Industry/Entity Type

Health And Wellness

Contact Information for Business Card

Address is : 482 Marlow Ave E
Toronto, ON K3T 8R2
website: www.brightvaleremedies.com

Font styles to use
Serif

Requirements
Must have
• clear, easy to read logo
Nice to have
• contrasting colors
Should not have
• we want to stay away from marijuana leaf

```html
<!DOCTYPE html>
<html lang="en">
<head>
<meta charset="utf-8">
<title>Brightvale Remedies – Business Cards</title>
<link rel="stylesheet" href="https://fonts.googleapis.com/css2?family=Tinos:wght@400;700&display=swap">
<style>
  :root {
    --page-bg: #f1ece4;
    --card-white: #ffffff;
    --leaf-green: #7cc242;
    --leaf-green-deep: #6ab22f;
    --sky-blue: #1fa6e2;
    --sky-blue-deep: #118fd0;
    --brand-ink: #1b8fc9;
    --brand-dot: #7cc242;
    --text-light: #ffffff;
    --shadow: rgba(40, 30, 20, 0.28);
  }
  * { box-sizing: border-box; margin: 0; padding: 0; }
  html, body {
    width: 1200px;
    height: 916px;
    overflow: hidden;
    background: var(--page-bg);
  }
  .canvas {
    position: relative;
    width: 1200px;
    height: 916px;
  }
  .business-card {
    position: absolute;
    width: 560px;
    height: 320px;
    border-radius: 28px;
    overflow: hidden;
    background: var(--card-white);
    box-shadow: 6px 10px 22px var(--shadow);
    font-family: "Tinos", "Times New Roman", serif;
  }
  .business-card--green { left: 70px; top: 90px; }
  .business-card--blue { left: 570px; top: 500px; }
  .card-backdrop {
    position: absolute;
    inset: 0;
    width: 100%;
    height: 100%;
  }
  .brand-mark {
    position: absolute;
    left: 34px;
    top: 112px;
    width: 230px;
    display: flex;
    align-items: center;
    gap: 12px;
  }
  .brand-dot {
    flex: none;
    width: 26px;
    height: 26px;
    border-radius: 50%;
    background: var(--brand-dot);
  }
  .brand-name {
    font-size: 30px;
    font-weight: 700;
    line-height: 1.1;
    color: var(--brand-ink);
  }
  .card-details {
    position: absolute;
    right: 28px;
    top: 0;
    width: 270px;
    height: 100%;
    color: var(--text-light);
    text-align: center;
  }
  .card-website {
    position: absolute;
    top: 26px;
    right: 0;
    font-size: 17px;
    white-space: nowrap;
  }
  .home-icon {
    position: absolute;
    top: 92px;
    left: 50%;
    transform: translateX(-50%);
    width: 30px;
    height: 30px;
  }
  .card-address {
    position: absolute;
    top: 152px;
    left: 0;
    right: 0;
    font-size: 25px;
    line-height: 58px;
    font-style: normal;
    white-space: nowrap;
    text-shadow: 0 0 6px rgba(255,255,255,0.55);
  }
</style>
</head>
<body>
<main class="canvas">

  <section class="business-card business-card--green">
    <svg class="card-backdrop" viewBox="0 0 560 320" preserveAspectRatio="none" aria-hidden="true">
      <defs>
        <linearGradient id="green-fade" x1="1" y1="0" x2="0.25" y2="1">
          <stop offset="0" stop-color="var(--leaf-green-deep)"/>
          <stop offset="0.55" stop-color="var(--leaf-green)"/>
          <stop offset="1" stop-color="#ffffff"/>
        </linearGradient>
        <linearGradient id="white-fade-green" x1="0" y1="0" x2="0" y2="1">
          <stop offset="0.6" stop-color="#ffffff" stop-opacity="0"/>
          <stop offset="1" stop-color="var(--leaf-green)" stop-opacity="0.9"/>
        </linearGradient>
      </defs>
      <rect width="560" height="320" fill="url(#white-fade-green)"/>
      <path d="M250,0 H560 V320 H290 C250,270 300,190 310,130 C318,80 290,30 250,0 Z" fill="url(#green-fade)"/>
    </svg>
    <div class="brand-mark">
      <span class="brand-dot"></span>
      <span class="brand-name">Brightvale Remedies</span>
    </div>
    <div class="card-details">
      <p class="card-website">www.brightvaleremedies.com</p>
      <svg class="home-icon" viewBox="0 0 30 30" aria-hidden="true">
        <rect x="3" y="3" width="24" height="24" rx="6" transform="rotate(45 15 15) scale(0.85) translate(2.6 2.6)" fill="#ffffff"/>
        <path d="M8 15 L15 8.5 L22 15 H19.5 V21 H10.5 V15 Z" fill="var(--leaf-green)"/>
        <rect x="13.5" y="17" width="3" height="4" fill="#ffffff"/>
      </svg>
      <address class="card-address">482 Marlow Ave E<br>Toronto, ON K3T 8R2</address>
    </div>
  </section>

  <section class="business-card business-card--blue">
    <svg class="card-backdrop" viewBox="0 0 560 320" preserveAspectRatio="none" aria-hidden="true">
      <defs>
        <linearGradient id="blue-fade" x1="1" y1="0" x2="0.25" y2="1">
          <stop offset="0" stop-color="var(--sky-blue-deep)"/>
          <stop offset="0.55" stop-color="var(--sky-blue)"/>
          <stop offset="1" stop-color="#ffffff"/>
        </linearGradient>
        <linearGradient id="white-fade-blue" x1="0" y1="0" x2="0" y2="1">
          <stop offset="0.6" stop-color="#ffffff" stop-opacity="0"/>
          <stop offset="1" stop-color="var(--sky-blue)" stop-opacity="0.9"/>
        </linearGradient>
      </defs>
      <rect width="560" height="320" fill="url(#white-fade-blue)"/>
      <path d="M250,0 H560 V320 H290 C250,270 300,190 310,130 C318,80 290,30 250,0 Z" fill="url(#blue-fade)"/>
    </svg>
    <div class="brand-mark">
      <span class="brand-dot"></span>
      <span class="brand-name">Brightvale Remedies</span>
    </div>
    <div class="card-details">
      <p class="card-website">www.brightvaleremedies.com</p>
      <svg class="home-icon" viewBox="0 0 30 30" aria-hidden="true">
        <rect x="3" y="3" width="24" height="24" rx="6" transform="rotate(45 15 15) scale(0.85) translate(2.6 2.6)" fill="#ffffff"/>
        <path d="M8 15 L15 8.5 L22 15 H19.5 V21 H10.5 V15 Z" fill="var(--leaf-green)"/>
        <rect x="13.5" y="17" width="3" height="4" fill="#ffffff"/>
      </svg>
      <address class="card-address">482 Marlow Ave E<br>Toronto, ON K3T 8R2</address>
    </div>
  </section>

</main>
</body>
</html>
```